RDW Drifting Marigold, American Quarter Horse Stallion Stud Services

Advertisement for stud service. I'd like to showcase how stunningly beautiful this horse is with the full-body pic and how sweet, gentle, and quiet he is with the other pic. I want two-sided cards with photos on both sides. Headshot (cropped) on front with info on management, contact #s, etc. Full-body, pairup.example-type pic on back with some information on his pedigree. I'd like something striking enough that even if people don't want the service, they keep the card.

Target Market(s)

Horse owners, horse breeders, horse trainers, equestrians

Contact Information for Business Card

Horse's name: RDW Drifting Marigold
Owner: Noreen Castell
Manager: Trudy Wexmoor
Phone: 208-555-0148
Pedigree information: Sire - Oaks Bonne Lucette, Dam - Quiet Dancing Lorabel
Sire's parents: Brightwater Tam 41 (sire) and Cedar Gentle Lass (dam)
Dam's parents: Shez Dorabel (sire) and Bold Hearted Rhyme (dam)

Font styles to use
Sans Serif

Requirements
Must have
• Rich, distinctive look. Should be a stand-out card; one that people keep even if they're not interested in the service.
Nice to have
• Pedigree information displayed in a family-tree arrangement. The horse is black, so I am picturing cards that are mostly black, probably with white or off-white (cream-colored) lettering. In fact, the horse has what's known as the cream-color gene, so maybe cream-colored would be better.

```html
<!DOCTYPE html>
<html lang="en">
<head>
<meta charset="utf-8">
<title>RDW Drifting Marigold – Stud Service Cards</title>
<link rel="stylesheet" href="https://fonts.googleapis.com/css2?family=Jost:wght@400;600&display=swap">
<style>
  :root {
    --backdrop: #e7e4df;
    --card: #3b3a38;
    --ink: #f4efe4;
    --shadow: rgba(0,0,0,0.28);
  }
  * { box-sizing: border-box; margin: 0; padding: 0; }
  html, body { width: 1200px; height: 1200px; overflow: hidden; }
  body {
    background: var(--backdrop);
    font-family: "Jost", "Century Gothic", sans-serif;
    color: var(--ink);
    position: relative;
  }
  .card {
    position: absolute;
    left: 160px;
    width: 880px;
    height: 503px;
    background: var(--card);
    overflow: hidden;
    box-shadow: 0 10px 24px var(--shadow);
  }
  .card--back { top: 76px; }
  .card--front { top: 621px; }

  /* Back: pedigree */
  .pedigree { position: absolute; inset: 0; }
  .pedigree__lines { position: absolute; inset: 0; }
  .pedigree__lines path { fill: none; stroke: var(--ink); stroke-width: 3; }
  .ped-text {
    position: absolute;
    font-size: 21px;
    line-height: 27px;
    font-weight: 400;
    white-space: nowrap;
  }
  .ped-sire-parents { left: 46px; top: 172px; }
  .ped-dam-parents { right: 410px; top: 172px; text-align: right; }
  .ped-sire { left: 52px; top: 252px; }
  .ped-dam { right: 410px; top: 252px; text-align: right; }
  .horse-name--back {
    position: absolute;
    left: 96px;
    top: 334px;
    font-size: 31px;
    font-weight: 600;
    white-space: nowrap;
  }
  .photo--full-body {
    position: absolute;
    left: 508px;
    top: 56px;
    width: 348px;
    height: 388px;
    background: linear-gradient(180deg, #9fb2bf 0%, #8c8f73 32%, #5d8a3c 55%, #1c1c1e 70%, #c9bba2 100%);
  }

  /* Front: contact */
  .horse-name--front {
    position: absolute;
    left: 40px;
    top: 112px;
    font-size: 31px;
    font-weight: 600;
    white-space: nowrap;
  }
  .contact {
    position: absolute;
    left: 40px;
    top: 162px;
    font-size: 24px;
    line-height: 36px;
    display: grid;
    grid-template-columns: 122px auto;
    column-gap: 6px;
    white-space: nowrap;
  }
  .contact__label { font-weight: 400; }
  .contact__value { font-weight: 400; }
  .contact__icon { width: 22px; height: 22px; margin-top: 7px; }
  .contact__icon circle, .contact__icon path { fill: none; stroke: var(--ink); stroke-width: 2; }
  .photo--headshot {
    position: absolute;
    right: 0;
    top: 0;
    width: 420px;
    height: 503px;
    background: linear-gradient(160deg, #6d7f8f 0%, #2a2420 30%, #1a1614 60%, #b9a88c 100%);
  }
</style>
</head>
<body>

<section class="card card--back" aria-label="Card back: pedigree">
  <div class="pedigree">
    <svg class="pedigree__lines" width="880" height="503" viewBox="0 0 880 503" aria-hidden="true">
      <path d="M110 228 V248"/>
      <path d="M415 228 V248"/>
      <path d="M120 292 V312 H405 V292"/>
      <path d="M235 312 V330"/>
    </svg>
    <div class="ped-text ped-sire-parents">Brightwater Tam 41<br>&amp; Cedar Gentle Lass</div>
    <div class="ped-text ped-dam-parents">Shez Dorabel<br>&amp; Bold Hearted Rhyme</div>
    <div class="ped-text ped-sire">Oaks Bonne Lucette</div>
    <div class="ped-text ped-dam">Quiet Dancing Lorabel</div>
    <div class="horse-name--back">RDW Drifting Marigold</div>
  </div>
  <div class="photo--full-body" role="img" aria-label="Full-body photo of the black stallion standing on a lead in a grassy yard"></div>
</section>

<section class="card card--front" aria-label="Card front: contact">
  <div class="horse-name--front">RDW Drifting Marigold</div>
  <div class="contact">
    <span class="contact__label">Owner:</span><span class="contact__value">Noreen Castell</span>
    <span class="contact__label">Manager:</span><span class="contact__value">Trudy Wexmoor</span>
    <svg class="contact__icon" viewBox="0 0 22 22" aria-label="Phone">
      <circle cx="11" cy="11" r="9.5"/>
      <path d="M7.5 6.5 l2 -0.5 l1 2.5 l-1.3 1 q1 2.3 3.3 3.3 l1 -1.3 l2.5 1 l-0.5 2 q-5.5 0.5 -8 -8z"/>
    </svg>
    <span class="contact__value">208-555-0148</span>
  </div>
  <div class="photo--headshot" role="img" aria-label="Cropped headshot of the black stallion wearing a western bridle in a sandy arena"></div>
</section>

</body>
</html>
```